Business Card Design for Contracting

I need a Busines card design for a new Busines (sole trader) based in Sydney, Australia. The business has been set up so I can contract my services to companies. The service I provide is mainly in the civil engineering discipline with the services that can be provided being contract project management, contract estimating, contract time controls and contract financial controls. I would like the design to have the colour blue used.

Target Market(s)

Large to medium Construction companies.

Industry/Entity Type

Construction

Contact Information for Business Card

Pelloway Civil Engineering Services
P.O. Box 418
Brambleford, NSW, 2093

Mobile: 0412 958 231

Email: marcus.pelloway@pcvx.com.au
Web: PCVX.com.au

Font styles to use
Sans Serif

Colors
0493ce
34a6d7
85cae6

Requirements
Must have
• my project must have my name and qualification:
• Marcus Pelloway
• BE (Civil), MTRQAust.

```html
<!DOCTYPE html>
<html lang="en">
<head>
<meta charset="utf-8">
<title>Pelloway Civil Engineering Services – Business Card</title>
<link rel="stylesheet" href="https://fonts.googleapis.com/css2?family=Open+Sans:wght@400;600&family=Roboto+Condensed:wght@700&display=swap">
<style>
  :root {
    --page-bg: #e9ebee;
    --card-bg: #fbfcfd;
    --card-edge: #d6dbe0;
    --brand-blue: #0b5d92;
    --band-blue: #0b5e95;
    --text-grey: #4a4f55;
    --rule-grey: #7d8186;
    --band-text: #e6eff6;
  }
  html, body {
    margin: 0;
    width: 1200px;
    height: 970px;
    overflow: hidden;
    background: var(--page-bg);
  }
  .card {
    position: absolute;
    left: 100px;
    top: 207px;
    width: 1000px;
    height: 556px;
    background: var(--card-bg);
    border: 1px solid var(--card-edge);
    border-radius: 26px;
    overflow: hidden;
    box-shadow: 0 14px 40px rgba(30, 45, 60, 0.12);
    font-family: "Open Sans", sans-serif;
    text-align: center;
  }
  .brand-square {
    position: absolute;
    left: 470px;
    top: 90px;
    width: 60px;
    height: 60px;
    background: var(--brand-blue);
  }
  .brand-name {
    position: absolute;
    left: 0;
    width: 100%;
    margin: 0;
    color: var(--brand-blue);
    font-weight: 600;
    text-transform: uppercase;
  }
  .brand-name .line-main {
    position: absolute;
    left: 0;
    width: 100%;
    top: 190px;
    font-size: 31px;
    letter-spacing: 2px;
  }
  .brand-name .line-sub {
    position: absolute;
    left: 0;
    width: 100%;
    top: 236px;
    font-size: 20px;
    letter-spacing: 6px;
  }
  .services-rule {
    position: absolute;
    top: 250px;
    height: 2px;
    background: var(--rule-grey);
  }
  .services-rule.left { left: 174px; width: 218px; }
  .services-rule.right { left: 612px; width: 218px; }
  .holder {
    position: absolute;
    left: 0;
    width: 100%;
    top: 356px;
    margin: 0;
    font-size: 22px;
    color: var(--brand-blue);
  }
  .holder-name {
    font-family: "Roboto Condensed", sans-serif;
    font-weight: 700;
    font-size: 29px;
  }
  .holder-quals { font-weight: 400; }
  .contact {
    position: absolute;
    left: 0;
    width: 100%;
    margin: 0;
    color: var(--text-grey);
  }
  .contact.phone { top: 418px; font-size: 24px; }
  .contact.email { top: 456px; font-size: 21px; }
  .address-band {
    position: absolute;
    left: 0;
    bottom: 0;
    width: 100%;
    height: 56px;
    background: var(--band-blue);
    color: var(--band-text);
    font-size: 22px;
    line-height: 56px;
    word-spacing: 2px;
  }
  .address-band .sep { margin: 0 12px; }
</style>
</head>
<body>
  <div class="card">
    <div class="brand-square"></div>
    <h1 class="brand-name">
      <span class="line-main">Pelloway Civil Engineering</span>
      <span class="line-sub">Services</span>
    </h1>
    <div class="services-rule left"></div>
    <div class="services-rule right"></div>

    <p class="holder"><span class="holder-name">Marcus Pelloway</span> <span class="holder-quals">/ BE (Civil), MTRQAust.</span></p>
    <p class="contact phone">0412 958 231</p>
    <p class="contact email">marcus@pelloway.net.au</p>

    <div class="address-band">P.O. Box 418<span class="sep">|</span>Brambleford<span class="sep">|</span>NSW<span class="sep">|</span>2093</div>
  </div>
</body>
</html>
```